Photography Business Card Design

I want a simple,classy design using a logo and simple font such as minion pro or similar. I have attached a logo that I quite like or am open to something similar. On the back of the card I would like the attached photo possibly with my website address on it some where. I want a matt black with silver or grey print. Possibly have the logo off to one side with the words Daniel Festerby Photography stacked on top of each other
Updates
I am very sorry that some how I forgot to put my facebook address on the details section, www.socialpage.example/DanielFesterbyPhotography
If this could be include on the card as well.
Industry/Entity Type
Business
Contact Information for Business Card
Daniel Festerby Photography
www.danielfesterbyphotography.example.au
Email: danielfesterby@wirenest.example
Phone: +61 (0)427 318 502
Logo Text
Logo styles of interest
Abstract Logo
Look and feel

```html
<!DOCTYPE html>
<html lang="en">
<head>
<meta charset="utf-8">
<title>Photography Business Card V2 – Daniel Festerby Photography</title>
<link rel="stylesheet" href="https://fonts.googleapis.com/css2?family=Bebas+Neue&family=Tinos&family=Arimo&display=swap">
<style>
  :root {
    --board: #c9c9c9;
    --ink: #111111;
    --orange: #f7941d;
    --white: #ffffff;
    --photo-dark: #3a342e;
    --photo-mid: #8a7a66;
    --photo-light: #c9b89a;
  }
  * { margin: 0; padding: 0; box-sizing: border-box; }
  html, body { width: 1200px; height: 458px; overflow: hidden; }
  body { background: var(--board); position: relative; font-family: "Arimo", Arial, sans-serif; }

  .board-title {
    position: absolute; left: 17px; top: 6px;
    font-family: "Bebas Neue", "Arial Narrow", sans-serif;
    font-size: 40px; letter-spacing: 3px; color: var(--ink); line-height: 1;
  }
  .side-label {
    position: absolute; top: 384px;
    font-family: "Bebas Neue", "Arial Narrow", sans-serif;
    font-size: 28px; letter-spacing: 3px; color: var(--ink); line-height: 1;
  }
  .side-label--back { left: 454px; }
  .side-label--front { left: 1040px; }

  .card { position: absolute; overflow: hidden; }
  .card--back { left: 17px; top: 64px; width: 570px; height: 302px; background: var(--orange); }
  .card--front { left: 608px; top: 66px; width: 573px; height: 298px; background: var(--white); }

  .shutter-photo {
    position: absolute; left: 266px; top: 6px; width: 300px; height: 300px; border-radius: 50%;
    background: radial-gradient(circle at 45% 40%, var(--photo-light) 0%, var(--photo-mid) 45%, var(--photo-dark) 100%);
  }
  .back-mark {
    position: absolute; left: 112px; top: 96px; width: 46px; height: 46px;
    border: 3px solid var(--white); border-radius: 50%;
  }
  .back-name {
    position: absolute; left: 168px; top: 110px;
    font-family: "Tinos", "Times New Roman", serif; font-size: 17px; color: var(--white);
  }
  .back-url {
    position: absolute; left: 140px; top: 150px;
    font-size: 14px; color: var(--white);
  }
  .back-rule {
    position: absolute; left: 108px; top: 172px; width: 462px; height: 2px; background: var(--white);
  }

  .front-mark {
    position: absolute; left: 58px; top: 60px; width: 46px; height: 46px;
    border: 3px solid var(--orange); border-radius: 50%;
  }
  .front-rule {
    position: absolute; left: 54px; top: 116px; width: 120px; height: 2px; background: var(--orange);
  }
  .front-name {
    position: absolute; left: 96px; top: 98px;
    font-family: "Tinos", "Times New Roman", serif; font-size: 42px; color: var(--ink); line-height: 1;
    letter-spacing: 1px;
  }
  .front-tagline {
    position: absolute; left: 262px; top: 140px;
    font-family: "Tinos", "Times New Roman", serif; font-size: 24px; color: var(--orange); line-height: 1;
  }
  .contact-line {
    position: absolute; left: 110px; display: flex; align-items: center; gap: 6px;
    font-size: 14px; color: var(--ink);
  }
  .contact-line--email { top: 190px; }
  .contact-line--phone { top: 218px; }
  .contact-line svg { display: block; }
</style>
</head>
<body>
  <h1 class="board-title">Artwork - Photography Business Card V2</h1>

  <section class="card card--back">
    <div class="shutter-photo" role="img" aria-label="Circular shutter-shaped montage of the photographer's work"></div>
    <div class="back-mark"></div>
    <span class="back-name">Daniel Festerby Photography</span>
    <span class="back-url">www.danielfesterbyphotography.example.au</span>
    <div class="back-rule"></div>
  </section>

  <section class="card card--front">
    <div class="front-mark"></div>
    <div class="front-rule"></div>
    <p class="front-name">Daniel Festerby</p>
    <p class="front-tagline">Photography</p>
    <p class="contact-line contact-line--email">
      <svg width="14" height="10" viewBox="0 0 14 10" aria-hidden="true">
        <rect x="0.5" y="0.5" width="13" height="9" fill="none" stroke="#111" />
        <polyline points="0.5,0.5 7,5.5 13.5,0.5" fill="none" stroke="#111" />
      </svg>
      <span>: danielfesterby@wirenest.example</span>
    </p>
    <p class="contact-line contact-line--phone">
      <svg width="10" height="14" viewBox="0 0 10 14" aria-hidden="true">
        <rect x="1" y="0.5" width="8" height="13" rx="1.5" fill="#111" />
        <rect x="2.5" y="2" width="5" height="8" fill="#fff" />
      </svg>
      <span>: +61 (0)427 318 502</span>
    </p>
  </section>

  <span class="side-label side-label--back">Back Side</span>
  <span class="side-label side-label--front">Front Side</span>
</body>
</html>
```